PPT template for boutique strategic planning, accounting and taxation firm

We are a boutique firm that provides strategic, accounting and tax advice to our clients. The work we are doing is increasingly strategic work and we are required to produce reports and presentations and our current templates are simply not sufficient.
As you can see from the examples attached, we have very limited skills in house re design! We have attached a PPT document and word document (that should be PPT) that we use regularly as examples of the content. Excel worksheets are regularly embedded into the presentation (in both blue and orange - see below re colours)
Not specific to one area but typically these clients are famous for their own brand and are creating value in their industry through creating their own brand and we want to produce documents of a similar standard.
A Powerpoint Document Slide Template
Cover page layout, back page, intermediate page heading, in colours and styles based on the logo, title styles, and an intermediate or chapter heading slide style. Many of our presentations contain slides with tables, diagrams, flowcharts and text, including simple lists of bullet points. As above, you will see in our style guide that we have three coloured logos – we would like one version in blue and one version in orange please. Again, the cover should be bold and draw attention but remain professional.
We are looking for something that works in both 4:3 and 16:9 (or two templates please)
We like a clear professional and simple look.
Deliverable: PowerPoint template file (.potx extension) for PowerPoint 2007 with at least a “cover” layout, a “title and content” layout, and a simplified slide layout, as well as “back cover”. Please embed any fonts used.
Target Market(s)
Many of our clients are retail clients or have strong brands of their own.
Industry/Entity Type
Accounting
Requirements
Must have
- Harrowby & Co logo on each page.
Must have a cover page (please be bold but professional)
A selection of "standard" slides - dot points, detailed written content, example diagrams, flow charts etc.
A back cover
Nice to have
- We would like to have a copy done in both the blue and orange versions attached. Happy for the winner to complete the other colour after the winner is selected.
Prefer Arial logo but open to suggestions. Must be easy to read and professional
Should not have
- Nothing cartoonish

```html
<!DOCTYPE html>
<html lang="en">
<head>
<meta charset="utf-8">
<title>Harrowby &amp; Co – Presentation Template Overview</title>
<link href="https://fonts.googleapis.com/css2?family=Montserrat:wght@400;600;700;800&family=Open+Sans:wght@400;600&display=swap" rel="stylesheet">
<style>
:root{
  --ink:#1d1d1f;
  --text:#3a3a3a;
  --muted:#7a7a7a;
  --board:#000;
  --blue-deep:#0f5ea8;
  --blue:#1e78c8;
  --blue-mid:#3a9bdc;
  --blue-light:#6cc3ee;
  --blue-pale:#bfe4f7;
  --yellow:#f4e21a;
  --grey:#d9d9d9;
  --grey-light:#ededed;
  --white:#fff;
}
*{box-sizing:border-box;margin:0;padding:0}
html,body{width:789px;height:1200px;overflow:hidden;background:var(--board)}
.board{position:relative;width:789px;height:1200px;background:var(--board);font-family:"Open Sans",Arial,sans-serif;color:var(--text)}
.slide{position:absolute;width:245px;height:184px;background:var(--white);overflow:hidden}
.slide.content::before{content:"";position:absolute;left:0;top:0;width:92px;height:3px;background:var(--blue)}
.title{position:absolute;left:26px;top:14px;font:700 7px/1.1 "Montserrat",Arial,sans-serif;color:var(--ink);text-transform:uppercase;letter-spacing:.1px}
.abs{position:absolute}
.foot{position:absolute;left:0;bottom:0;width:245px;height:34px}
.foot svg{position:absolute;inset:0;width:100%;height:100%}
.foot .web{position:absolute;left:20px;bottom:7px;font:400 3.6px "Open Sans",Arial,sans-serif;color:var(--white)}
.foot .pg{position:absolute;right:18px;bottom:7px;font:400 3.6px "Open Sans",Arial,sans-serif;color:var(--white)}
.brand{display:inline-block;font-family:"Open Sans",Arial,sans-serif;font-weight:600;color:var(--blue);white-space:nowrap}
.foot .brand{position:absolute;left:50%;bottom:5.5px;transform:translateX(-50%);font-size:5.5px;color:var(--white)}
.brand.lg{font-size:14px}
.brand.md{font-size:7.5px}
.cover-band{position:absolute;left:0;width:245px}
.cover-title{position:absolute;left:0;width:245px;text-align:center;font:800 10px "Montserrat",Arial,sans-serif;color:var(--white)}
.cover-sub{position:absolute;left:0;width:245px;text-align:center;font:700 5.4px "Montserrat",Arial,sans-serif;color:var(--yellow)}
.cover-web{position:absolute;left:0;width:245px;text-align:center;font:400 3.8px "Open Sans",Arial,sans-serif;color:var(--ink)}
.media{position:absolute}
.copy{font-size:3.2px;line-height:1.45;text-align:justify;color:var(--text)}
.copy p{margin-bottom:3px}
.client-table{position:absolute;left:25px;top:38px;width:196px;border-collapse:collapse;font-size:3px}
.client-table th{background:var(--blue);color:var(--white);font-weight:600;padding:2px 1px;height:11px;border-right:1px solid var(--white);line-height:1.1}
.client-table td{height:7px;border-right:1px solid var(--white)}
.client-table tr:nth-child(odd) td{background:var(--grey)}
.client-table tr:nth-child(even) td{background:var(--grey-light)}
.principles{position:absolute;left:98px;list-style:none;font-size:3.7px;line-height:9.6px;color:var(--text)}
.caption{position:absolute;width:46px;text-align:center;font-size:3.6px;line-height:1.35;color:var(--text)}
.caption b{font-weight:700;color:var(--ink)}
.bubble-label{font:600 2.8px "Open Sans",Arial,sans-serif;fill:var(--white)}
.legend{position:absolute;left:40px;top:136px;display:flex;gap:5px;font-size:3.2px;color:var(--text)}
.legend span::before{content:"";display:inline-block;width:3px;height:3px;margin-right:1.5px;background:var(--c)}
.numbered{position:absolute;list-style:none;font:600 4px "Open Sans",Arial,sans-serif;color:var(--ink);text-transform:uppercase}
.numbered li{display:flex;align-items:center;gap:8px;height:21px}
.numbered li b{display:flex;align-items:center;justify-content:center;width:13px;height:13px;border-radius:50%;background:var(--blue);color:var(--white);font-size:4px}
.process{position:absolute;left:26px;top:34px;width:196px;border-collapse:collapse;font-size:2.6px;table-layout:fixed}
.process th{color:var(--white);font-weight:700;padding:1.5px 1px;font-size:3.2px}
.process .phase th{background:var(--blue-light)}
.process .step th{background:var(--blue);font-size:2.8px;height:9px}
.process td{vertical-align:top;padding:2px 2px;line-height:4.2px;color:var(--text);background:#f6f6f6;border-right:1px solid var(--white)}
.process .band th{background:var(--blue-light);height:6px}
</style>
</head>
<body>
<svg width="0" height="0" style="position:absolute" aria-hidden="true">
  <defs>
    <linearGradient id="waveLight" x1="0" y1="0" x2="0" y2="1">
      <stop offset="0" stop-color="#cfeaf9"/><stop offset="1" stop-color="#6cc3ee"/>
    </linearGradient>
    <linearGradient id="waveDeep" x1="0" y1="0" x2="0" y2="1">
      <stop offset="0" stop-color="#2b8ad6"/><stop offset="1" stop-color="#0f5ea8"/>
    </linearGradient>
    <linearGradient id="coverBlue" x1="0" y1="0" x2="0" y2="1">
      <stop offset="0" stop-color="#1a6fc0"/><stop offset=".6" stop-color="#2e8ad8"/><stop offset="1" stop-color="#8fd0f3"/>
    </linearGradient>
    <marker id="head" viewBox="0 0 10 10" refX="4" refY="5" markerWidth="2.2" markerHeight="2.2" orient="auto">
      <path d="M0 0L10 5L0 10Z" fill="context-stroke"/>
    </marker>
    <symbol id="wave" viewBox="0 0 245 34" preserveAspectRatio="none">
      <path d="M0 6Q122 24 245 6L245 34L0 34Z" fill="url(#waveLight)"/>
      <path d="M0 15Q122 31 245 15L245 34L0 34Z" fill="url(#waveDeep)"/>
    </symbol>
  </defs>
</svg>

<main class="board">

  <!-- 1 Name cover -->
  <section class="slide logo-cover" style="left:17px;top:17px;background:radial-gradient(ellipse at center,#ffffff 35%,#d6d6d6 100%)">
    <div class="abs" style="left:0;top:82px;width:245px;text-align:center"><span class="brand lg">Harrowby &amp; Co</span></div>
  </section>

  <!-- 2 Title cover -->
  <section class="slide title-cover" style="left:272px;top:17px;background:linear-gradient(#fff,#e6e6e6)">
    <div class="abs" style="left:0;top:18px;width:245px;text-align:center"><span class="brand md">Harrowby &amp; Co</span></div>
    <svg class="cover-band" style="top:38px" width="245" height="122" viewBox="0 0 245 122">
      <path d="M0 0H245V92Q170 92 122 120Q75 92 0 92Z" fill="url(#coverBlue)"/>
    </svg>
    <div class="cover-title" style="top:82px">THE BUSINESS IMPROVEMENT PROCESS</div>
    <div class="cover-sub" style="top:96px">AN INTRODUCTION</div>
    <div class="cover-web" style="top:166px">www.harrowbyco.com</div>
  </section>

  <!-- 3 Text and image -->
  <section class="slide content" style="left:528px;top:17px">
    <h2 class="title">Concept plus presentation powerful mission 1</h2>
    <div class="media" role="img" aria-label="Photograph of a city office tower at dusk" style="left:27px;top:40px;width:85px;height:70px;background:linear-gradient(160deg,#3c5d8a,#1b2c4d 60%,#c48a45)"></div>
    <div class="copy abs" style="left:125px;top:40px;width:106px">
      <p>The firm has forged a rigorous and dynamic approach to the methodology of client research. By overcoming previous pitfalls that held the industry back, the team has propelled the frontier of business research to a new level.</p>
      <p>Essential to this approach are four proven pillars that drive growth, sharpen focus and build lasting value for every client we serve.</p>
      <p>Groundbreaking initiatives that have modernised the way research and planning are conducted.</p>
    </div>
    <div class="foot"><svg><use href="#wave"/></svg><span class="web">www.harrowbyco.com</span><span class="brand">Harrowby &amp; Co</span><span class="pg">1</span></div>
  </section>

  <!-- 4 World map -->
  <section class="slide content" style="left:17px;top:213px">
    <h2 class="title">More than 500+ satisfied client over the world</h2>
    <div class="media" role="img" aria-label="World map with client percentages by region" style="left:26px;top:34px;width:180px;height:100px;background:radial-gradient(ellipse at 50% 45%,#b8b8b8,#dcdcdc 70%,#fff 100%)"></div>
    <div class="foot"><svg><use href="#wave"/></svg><span class="web">www.harrowbyco.com</span><span class="brand">Harrowby &amp; Co</span><span class="pg">2</span></div>
  </section>

  <!-- 5 Clients table -->
  <section class="slide content" style="left:272px;top:213px">
    <h2 class="title">Some of our clients</h2>
    <table class="client-table">
      <thead><tr><th>Professional services</th><th>Transport</th><th>Distribution</th><th>Property / Construction</th><th>Retail</th><th>Manufacturing</th></tr></thead>
      <tbody>
        <tr><td></td><td></td><td></td><td></td><td></td><td></td></tr>
        <tr><td></td><td></td><td></td><td></td><td></td><td></td></tr>
        <tr><td></td><td></td><td></td><td></td><td></td><td></td></tr>
        <tr><td></td><td></td><td></td><td></td><td></td><td></td></tr>
        <tr><td></td><td></td><td></td><td></td><td></td><td></td></tr>
        <tr><td></td><td></td><td></td><td></td><td></td><td></td></tr>
        <tr><td></td><td></td><td></td><td></td><td></td><td></td></tr>
        <tr><td></td><td></td><td></td><td></td><td></td><td></td></tr>
        <tr><td></td><td></td><td></td><td></td><td></td><td></td></tr>
        <tr><td></td><td></td><td></td><td></td><td></td><td></td></tr>
        <tr><td></td><td></td><td></td><td></td><td></td><td></td></tr>
        <tr><td></td><td></td><td></td><td></td><td></td><td></td></tr>
      </tbody>
    </table>
    <div class="foot"><svg><use href="#wave"/></svg><span class="web">www.harrowbyco.com</span><span class="brand">Harrowby &amp; Co</span><span class="pg">3</span></div>
  </section>

  <!-- 6 Key success principles -->
  <section class="slide content" style="left:528px;top:213px">
    <h2 class="title">Key success principles</h2>
    <svg class="abs" style="left:10px;top:34px" width="112" height="125" viewBox="0 0 100 112">
      <g stroke="#fff" stroke-width=".8">
        <circle cx="45" cy="68" r="42" fill="#cbeafa"/>
        <circle cx="45" cy="74" r="36" fill="#a6dcf6"/>
        <circle cx="45" cy="80" r="30" fill="#7fcbf0"/>
        <circle cx="45" cy="86" r="24" fill="#55b5e8"/>
        <circle cx="45" cy="92" r="18" fill="#3a9bdc"/>
        <circle cx="45" cy="98" r="12" fill="#237fcb"/>
        <circle cx="45" cy="104" r="6" fill="#0f5ea8"/>
      </g>
      <g font-family="Montserrat,Arial,sans-serif" font-size="4" font-weight="700" fill="#fff" text-anchor="middle">
        <text x="45" y="32">7</text><text x="45" y="43">6</text><text x="45" y="55">5</text><text x="45" y="67">4</text><text x="45" y="79">3</text><text x="45" y="91">2</text><text x="45" y="105">1</text>
      </g>
    </svg>
    <ol class="principles" style="top:56px">
      <li>Find and work with a trusted business adviser.</li>
      <li>Understand and drive economic value creation.</li>
      <li>Measure and improve free cash flow.</li>
      <li>Identify and improve the economic determinants.</li>
      <li>Sharpen and maintain focus.</li>
      <li>Measure and improve processes.</li>
      <li>Limit the number of strategic goals.</li>
    </ol>
    <div class="foot"><svg><use href="#wave"/></svg><span class="web">www.harrowbyco.com</span><span class="brand">Harrowby &amp; Co</span><span class="pg">4</span></div>
  </section>

  <!-- 7 Value of the entrepreneur -->
  <section class="slide content" style="left:17px;top:409px">
    <h2 class="title">The value of the entrepreneur</h2>
    <svg class="abs" style="left:0;top:40px" width="245" height="64" viewBox="0 0 245 64">
      <g stroke="#fff" stroke-width="2.5">
        <circle cx="72" cy="32" r="28" fill="#2f78bd"/>
        <circle cx="122" cy="32" r="28" fill="#3b95d6"/>
        <circle cx="172" cy="32" r="28" fill="#5bb8e6"/>
      </g>
    </svg>
    <p class="caption" style="left:49px;top:110px">Entrepreneurial<br><b>Abilities</b><br>create wealth</p>
    <p class="caption" style="left:99px;top:110px">Entrepreneurial<br><b>Attitudes</b><br>create wealth</p>
    <p class="caption" style="left:149px;top:110px">Entrepreneurial<br><b>Behaviours</b><br>create wealth</p>
    <div class="foot"><svg><use href="#wave"/></svg><span class="web">www.harrowbyco.com</span><span class="brand">Harrowby &amp; Co</span><span class="pg">5</span></div>
  </section>

  <!-- 8 What is entrepreneurship -->
  <section class="slide content" style="left:272px;top:409px">
    <h2 class="title">What is entrepreneurship</h2>
    <svg class="abs" style="left:0;top:30px" width="245" height="110" viewBox="0 0 245 110">
      <g stroke="#c9c9c9" stroke-width="1.2" fill="none" marker-end="url(#head)">
        <path d="M82 42L100 30"/><path d="M144 30L160 42"/><path d="M160 78L143 88"/><path d="M100 88L84 78"/>
      </g>
      <g stroke="#e4f3fb" stroke-width="2.5">
        <circle cx="122" cy="26" r="18" fill="#5bb8e6"/>
        <circle cx="66" cy="60" r="19" fill="#2f78bd"/>
        <circle cx="178" cy="60" r="19" fill="#9ad7f3"/>
        <circle cx="122" cy="92" r="19" fill="#1f5f9e"/>
      </g>
      <g text-anchor="middle" class="bubble-label">
        <text x="122" y="36">Creative Innovation</text>
        <text x="66" y="63">Protecting Value</text>
        <text x="178" y="70">Strategic Planning</text>
        <text x="122" y="100">Leading and Managing</text><text x="122" y="104">Growth</text>
      </g>
    </svg>
    <div class="foot"><svg><use href="#wave"/></svg><span class="web">www.harrowbyco.com</span><span class="brand">Harrowby &amp; Co</span><span class="pg">6</span></div>
  </section>

  <!-- 9 Entrepreneurial attitudes -->
  <section class="slide content" style="left:528px;top:409px">
    <h2 class="title">Entrepreneurial attitudes</h2>
    <svg class="abs" style="left:30px;top:40px" width="190" height="92" viewBox="0 0 190 92">
      <rect x="12" y="10" width="22" height="80" fill="#1e6fbd"/><rect x="34" y="12" width="3" height="78" fill="#15528d"/>
      <rect x="44" y="42" width="22" height="48" fill="#2b8ad6"/><rect x="66" y="44" width="3" height="46" fill="#1f69a8"/>
      <rect x="78" y="6" width="22" height="84" fill="#3aa5e6"/><rect x="100" y="8" width="3" height="82" fill="#2b82b8"/>
      <rect x="110" y="12" width="22" height="78" fill="#6cc3ee"/><rect x="132" y="14" width="3" height="76" fill="#4e9ec6"/>
      <rect x="144" y="66" width="22" height="24" fill="#a8ddf6"/><rect x="166" y="68" width="3" height="22" fill="#82bcd8"/>
      <path d="M0 90H185" stroke="#d0d0d0" stroke-width=".6"/>
    </svg>
    <div class="legend">
      <span style="--c:#1e6fbd">Independence</span><span style="--c:#2b8ad6">Risk</span><span style="--c:#3aa5e6">Need Achievement</span><span style="--c:#6cc3ee">Simplicity</span><span style="--c:#a8ddf6">Success goals</span>
    </div>
    <div class="foot"><svg><use href="#wave"/></svg><span class="web">www.harrowbyco.com</span><span class="brand">Harrowby &amp; Co</span><span class="pg">7</span></div>
  </section>

  <!-- 10 Divider -->
  <section class="slide divider" style="left:17px;top:606px;background:linear-gradient(#1e78c8,#2f8ed9)">
    <div class="abs" style="left:0;top:18px;width:245px;text-align:center"><span class="brand md" style="color:var(--white)">Harrowby &amp; Co</span></div>
    <svg class="cover-band" style="top:40px" width="245" height="120" viewBox="0 0 245 120">
      <defs><linearGradient id="divBand" x1="0" y1="0" x2="0" y2="1"><stop offset="0" stop-color="#e8f6fd"/><stop offset=".5" stop-color="#8fd0f3"/><stop offset="1" stop-color="#3a9bdc"/></linearGradient></defs>
      <path d="M0 0Q122 10 245 0V80Q170 80 122 112Q75 80 0 80Z" fill="url(#divBand)"/>
    </svg>
    <div class="cover-title" style="top:82px;color:var(--white)">DIVIDER PAGES HERE</div>
    <div class="cover-sub" style="top:95px;color:var(--blue-deep);font-size:4.6px">YOUR PRESENTATION TITLE HERE</div>
    <div class="cover-web" style="top:168px;color:var(--white)">www.harrowbyco.com</div>
  </section>

  <!-- 11 Forces driving change -->
  <section class="slide content" style="left:272px;top:606px">
    <h2 class="title">Forces driving change</h2>
    <svg class="abs" style="left:0;top:28px" width="245" height="120" viewBox="0 0 245 120">
      <g stroke="#fff" stroke-width="1">
        <circle cx="40" cy="52" r="13" fill="#cfeaf9"/>
        <circle cx="66" cy="44" r="13" fill="#a6dcf6"/>
        <circle cx="93" cy="40" r="13" fill="#7fcbf0"/>
        <circle cx="120" cy="38" r="13" fill="#55b5e8"/>
        <circle cx="147" cy="40" r="13" fill="#3a9bdc"/>
        <circle cx="174" cy="44" r="13" fill="#2b82c8"/>
        <circle cx="200" cy="52" r="13" fill="#1f6fb2"/>
      </g>
      <g text-anchor="middle" class="bubble-label" style="fill:#1d4f80">
        <text x="40" y="52">Economic</text><text x="40" y="56">Growth</text>
      </g>
      <g text-anchor="middle" class="bubble-label">
        <text x="66" y="44">Market</text><text x="66" y="48">Regulations</text>
        <text x="93" y="40">Changing</text><text x="93" y="44">Markets</text>
        <text x="120" y="38">Emerging</text><text x="120" y="42">Technology</text>
        <text x="147" y="40">Global</text><text x="147" y="44">Competition</text>
        <text x="174" y="44">Government</text><text x="174" y="48">Regulation</text>
        <text x="200" y="52">Technology</text><text x="200" y="56">Change</text>
      </g>
      <rect x="98" y="66" width="44" height="11" fill="#8a8a8a"/>
      <text x="120" y="73.5" text-anchor="middle" font-family="Montserrat,Arial,sans-serif" font-weight="700" font-size="5" fill="#fff" letter-spacing="1">FIRMS</text>
      <path d="M26 82H226" stroke="#b5b5b5" stroke-width=".5" stroke-dasharray="2 1.5"/>
      <text x="26" y="80" font-size="2.6" fill="#777" font-family="Open Sans,Arial,sans-serif">EXTERNAL FORCES</text>
      <text x="26" y="86.5" font-size="2.6" fill="#777" font-family="Open Sans,Arial,sans-serif">INTERNAL FORCES</text>
      <g stroke="#fff" stroke-width="1">
        <circle cx="68" cy="101" r="14" fill="#7fcbf0"/>
        <circle cx="96" cy="103" r="14" fill="#55b5e8"/>
        <circle cx="124" cy="104" r="14" fill="#3a9bdc"/>
        <circle cx="152" cy="103" r="14" fill="#2b82c8"/>
        <circle cx="180" cy="101" r="14" fill="#1f5f9e"/>
      </g>
      <g text-anchor="middle" class="bubble-label">
        <text x="68" y="101">Increasing</text><text x="68" y="105">Costs</text>
        <text x="96" y="103">Skills</text><text x="96" y="107">Shortage</text>
        <text x="124" y="104">New</text><text x="124" y="108">Competitors</text>
        <text x="152" y="103">Aging</text><text x="152" y="107">Workforce</text>
        <text x="180" y="101">Workforce</text><text x="180" y="105">Change</text>
      </g>
    </svg>
    <div class="foot"><svg><use href="#wave"/></svg><span class="web">www.harrowbyco.com</span><span class="brand">Harrowby &amp; Co</span><span class="pg">9</span></div>
  </section>

  <!-- 12 Locus of control -->
  <section class="slide content" style="left:528px;top:606px">
    <h2 class="title">Locus of control</h2>
    <p class="abs" style="left:26px;top:33px;font-size:4.4px;color:var(--ink)">Where does the control lie?</p>
    <svg class="abs" style="left:0;top:36px" width="245" height="110" viewBox="0 0 245 110">
      <g stroke="#e4f3fb" stroke-width="2.5">
        <circle cx="128" cy="28" r="20" fill="#55b5e8"/>
        <circle cx="79" cy="62" r="20" fill="#2f78bd"/>
        <circle cx="176" cy="62" r="17" fill="#a6dcf6"/>
        <circle cx="128" cy="86" r="20" fill="#1f5f9e"/>
      </g>
      <g fill="#fff"><rect x="121" y="22" width="3" height="6"/><rect x="126" y="18" width="3" height="10"/><rect x="131" y="14" width="3" height="14"/></g>
      <rect x="170" y="54" width="12" height="9" rx="1" fill="none" stroke="#fff" stroke-width=".8"/>
      <g text-anchor="middle" font-family="Open Sans,Arial,sans-serif" font-size="3.6" fill="#fff">
        <text x="128" y="40">Economy</text><text x="79" y="67">Customers</text><text x="176" y="70">Banks</text><text x="128" y="98">Competition</text>
      </g>
    </svg>
    <div class="foot"><svg><use href="#wave"/></svg><span class="web">www.harrowbyco.com</span><span class="brand">Harrowby &amp; Co</span><span class="pg">10</span></div>
  </section>

  <!-- 13 Reasons why -->
  <section class="slide content" style="left:17px;top:802px">
    <h2 class="title">Reasons why</h2>
    <ol class="numbered" style="left:56px;top:65px">
      <li><b>1</b>Management</li>
      <li><b>2</b>Poor financial information and skills</li>
    </ol>
    <div class="foot"><svg><use href="#wave"/></svg><span class="web">www.harrowbyco.com</span><span class="brand">Harrowby &amp; Co</span><span class="pg">11</span></div>
  </section>

  <!-- 14 Creating or destroying value -->
  <section class="slide content" style="left:272px;top:802px">
    <h2 class="title">Are you creating or destroying value?</h2>
    <ol class="numbered" style="left:49px;top:46px">
      <li><b>1</b>Producing real profit</li>
      <li><b>2</b>Driving improvement in activity drivers</li>
      <li><b>3</b>Sharpening focus : customers, markets, products</li>
      <li><b>4</b>Process improvement</li>
    </ol>
    <div class="foot"><svg><use href="#wave"/></svg><span class="web">www.harrowbyco.com</span><span class="brand">Harrowby &amp; Co</span><span class="pg">12</span></div>
  </section>

  <!-- 15 Business improvement cycle -->
  <section class="slide content" style="left:528px;top:802px">
    <h2 class="title">Business improvement process</h2>
    <svg class="abs" style="left:0;top:30px" width="245" height="110" viewBox="0 0 245 110">
      <g fill="none" stroke-width="13" marker-end="url(#head)">
        <path d="M90 50A33 33 0 0 1 116 21" stroke="#6cc3ee"/>
        <path d="M128 21A33 33 0 0 1 156 47" stroke="#1e78c8"/>
        <path d="M156 59A33 33 0 0 1 130 87" stroke="#3a9bdc"/>
        <path d="M116 87A33 33 0 0 1 90 62" stroke="#a6dcf6"/>
      </g>
      <g font-family="Montserrat,Arial,sans-serif" font-weight="700" font-size="3.2" fill="#fff" text-anchor="middle">
        <text x="101" y="34" transform="rotate(-45 101 34)">EXPLORE</text>
        <text x="145" y="33" transform="rotate(45 145 33)">CHANGE</text>
        <text x="146" y="78" transform="rotate(-45 146 78)">GROW</text>
        <text x="100" y="78" transform="rotate(45 100 78)">REVIEW</text>
      </g>
    </svg>
    <div class="foot"><svg><use href="#wave"/></svg><span class="web">www.harrowbyco.com</span><span class="brand">Harrowby &amp; Co</span><span class="pg">13</span></div>
  </section>

  <!-- 16 Business improvement process table -->
  <section class="slide content" style="left:17px;top:998px">
    <h2 class="title">Business improvement process</h2>
    <table class="process">
      <tr class="phase"><th colspan="2">EXPLORE</th><th>CHANGE</th><th colspan="2">GROW</th><th>REVIEW</th></tr>
      <tr class="step"><th>Understanding</th><th>Planning</th><th>Strategic Actions</th><th>Process Improvement</th><th>Performance</th><th>Monitoring</th></tr>
      <tr>
        <td>Cash flow<br>Profit drivers<br>Key risks<br>Market review<br>Cost base</td>
        <td>Set goals<br>Key targets<br>Budget plan<br>Core values<br>Owner aims</td>
        <td>New pricing<br>Cost cuts<br>Sales focus<br>Team roles<br>Key hires</td>
        <td>Lean systems<br>Clear steps<br>Better data<br>Lower waste<br>Fast cycles</td>
        <td>Track profit<br>Weekly sales<br>Margin trend<br>Cash days<br>Staff output</td>
        <td>Monthly review<br>Board report<br>Next steps<br>Risk check<br>Reset goals</td>
      </tr>
      <tr class="band"><th colspan="6">SUSTAIN</th></tr>
      <tr>
        <td>Annual plan<br>Tax review<br>Cash buffer</td>
        <td>Brand value<br>Client care<br>Market share</td>
        <td>Team skills<br>Clear roles<br>Succession plan</td>
        <td>Growth plan<br>Exit options<br>Owner wealth</td>
        <td></td><td></td>
      </tr>
    </table>
    <div class="foot"><svg><use href="#wave"/></svg><span class="web">www.harrowbyco.com</span><span class="brand">Harrowby &amp; Co</span><span class="pg">14</span></div>
  </section>

  <!-- 17 Back cover -->
  <section class="slide back-cover" style="left:272px;top:998px;background:linear-gradient(#fff,#e6e6e6)">
    <div class="abs" style="left:0;top:18px;width:245px;text-align:center"><span class="brand md">Harrowby &amp; Co</span></div>
    <svg class="cover-band" style="top:38px" width="245" height="122" viewBox="0 0 245 122">
      <path d="M0 0H245V92Q170 92 122 120Q75 92 0 92Z" fill="url(#coverBlue)"/>
    </svg>
    <div class="cover-title" style="top:82px;font-size:11px">THANK YOU VERY MUCH</div>
    <div class="cover-sub" style="top:98px">YOUR PRESENTATION TITLE HERE</div>
    <div class="cover-web" style="top:166px">www.harrowbyco.com</div>
  </section>

</main>
</body>
</html>
```